Tallow Accounting Business Card design

We need a stand out business card design for Accounting practice based in Australia specialising in pubs, clubs and hotels. We help venues maximise margins, create time and manage cashflow. One club we have been working with for the last 6 months has increased revenue by 3% and margin by 5% in this time frame. We have a back office outsourced system that costs less than having a full time employee and also allows the venues the added benefit of:<br/>-using the office space to become a revenue generating opportunity. <br/>-a complete system to enhance governance, accountability and efficiency within their operation<br/>-52 weeks cover so no hassle to cover annual/sick .. leave<br/><br/>We would like to see designs that use the colours of our logo (green & blue).
Target Market(s)
Australian Pubs, Clubs & Hotels abookkeeping, accounting and tax services
Industry/Entity Type
Accountant
Contact Information for Business Card
Miriel Dawkes CPA
Principal
Accountant Tax Agent
Miriel@TallowAccounting.example.au
0418639174
www.tallowaccounting.example.au
Accounting / Payroll / Tax / SMSF / Technology
Colors
Designer to choose colors to be used in the design.
Look and feel
Each slider illustrates characteristics of the customer's brand and the style your logo design should communicate.

```html
<!DOCTYPE html>
<html lang="en">
<head>
<meta charset="utf-8">
<title>Tallow Accounting Business Card</title>
<link rel="stylesheet" href="https://fonts.googleapis.com/css2?family=Montserrat:wght@500;700;800&family=Roboto:wght@400&display=swap">
<style>
  :root {
    --bg: #e4e4e4;
    --card: #ffffff;
    --green: #137a3c;
    --blue: #24368f;
    --grey: #6d6d6d;
    --ink: #555555;
  }
  * { margin: 0; padding: 0; box-sizing: border-box; }
  html, body { width: 1200px; height: 930px; overflow: hidden; background: var(--bg); }
  .canvas { position: relative; width: 1200px; height: 930px; }
  .card {
    position: absolute;
    width: 560px; height: 340px;
    background: var(--card);
    border-radius: 22px;
    overflow: hidden;
    box-shadow: 0 4px 14px rgba(0,0,0,0.12);
  }
  .card--front { left: 80px; top: 80px; }
  .card--back { left: 560px; top: 500px; }

  .wordmark {
    display: flex; align-items: center;
    font-family: "Montserrat", sans-serif;
    font-weight: 800;
    color: var(--blue);
    white-space: nowrap;
  }
  .wordmark__dot { border-radius: 50%; background: var(--green); flex: none; }

  .card--front .wordmark { position: absolute; left: 0; right: 0; top: 100px; justify-content: center; gap: 14px; font-size: 38px; }
  .card--front .wordmark__dot { width: 34px; height: 34px; }

  .service-band {
    position: absolute; left: 0; right: 0; bottom: 36px; height: 44px;
    background: var(--green);
    display: flex; align-items: center; justify-content: center;
    font-family: "Montserrat", sans-serif; font-weight: 700; font-size: 18px;
    color: #fff; letter-spacing: 0.3px;
  }

  .card--back .wordmark { position: absolute; left: 28px; top: 170px; gap: 10px; font-size: 20px; }
  .card--back .wordmark__dot { width: 18px; height: 18px; }

  .divider { position: absolute; left: 284px; top: 86px; width: 1.5px; height: 150px; background: var(--green); }

  .contact { position: absolute; left: 302px; top: 96px; right: 20px; }
  .contact__name {
    font-family: "Montserrat", sans-serif; font-weight: 800; font-size: 18px;
    color: var(--blue); letter-spacing: 0.3px; white-space: nowrap;
  }
  .contact__name .first { color: var(--green); }
  .contact__role { font-family: "Roboto", sans-serif; font-size: 13px; color: var(--grey); margin-top: 4px; }
  .contact__list { list-style: none; margin-top: 14px; }
  .contact__item {
    display: flex; align-items: center; gap: 7px;
    font-family: "Roboto", sans-serif; font-size: 12px; color: var(--ink);
    line-height: 22px; white-space: nowrap;
  }
  .contact__item--web { color: var(--green); }
  .contact__icon { width: 11px; height: 11px; flex: none; }
</style>
</head>
<body>
<main class="canvas">

  <section class="card card--front" aria-label="Card front">
    <div class="wordmark"><span class="wordmark__dot"></span><span>Tallow Accounting</span></div>
    <div class="service-band">Accounting | Payroll | Tax | SMSF | Technology</div>
  </section>

  <section class="card card--back" aria-label="Card back">
    <div class="wordmark"><span class="wordmark__dot"></span><span>Tallow Accounting</span></div>
    <div class="divider"></div>
    <div class="contact">
      <p class="contact__name"><span class="first">MIRIEL</span> DAWKES CPA</p>
      <p class="contact__role">Principal</p>
      <ul class="contact__list">
        <li class="contact__item">
          <svg class="contact__icon" viewBox="0 0 24 24"><path d="M6.6 10.8a15 15 0 0 0 6.6 6.6l2.2-2.2a1 1 0 0 1 1-.25 11.4 11.4 0 0 0 3.6.57 1 1 0 0 1 1 1V20a1 1 0 0 1-1 1A17 17 0 0 1 3 4a1 1 0 0 1 1-1h3.5a1 1 0 0 1 1 1c0 1.25.2 2.45.57 3.57a1 1 0 0 1-.25 1z" fill="#137a3c"/></svg>
          0418639174
        </li>
        <li class="contact__item">
          <svg class="contact__icon" viewBox="0 0 24 24"><rect x="2" y="5" width="20" height="14" rx="1.5" fill="none" stroke="#137a3c" stroke-width="2"/><path d="M3 6l9 7 9-7" fill="none" stroke="#137a3c" stroke-width="2"/></svg>
          Miriel@TallowAccounting.example.au
        </li>
        <li class="contact__item contact__item--web">
          <svg class="contact__icon" viewBox="0 0 24 24"><circle cx="12" cy="12" r="10" fill="none" stroke="#137a3c" stroke-width="2"/><path d="M2 12h20M12 2c3 3 3 17 0 20M12 2c-3 3-3 17 0 20" fill="none" stroke="#137a3c" stroke-width="1.6"/></svg>
          www.tallowaccounting.example.au
        </li>
      </ul>
    </div>
  </section>

</main>
</body>
</html>
```